Ribbon Cutting Ceremony Invitation for Solar Company

Need 8.5 x 11 Ribbon Cutting Invitation Design to be used for digital and print. The design should be professional yet creative. It should showcase the theme of a ribbon cutting with some sort of style resembling solar energy. There could also be an option to include a placeholder for a photo of the facility, but that is up to your creative direction. Thanks designers!

Words that should be on it are below:

RIBBON CUTTING CEREMONY

WE FORMALLY INVITE YOU TO THE RIBBON CUTTING EVENT FOR THE NEW SOLAR SYSTEM @ SEABRAMBLE HOTEL AND RESORT.

DATE AND TIME

Use this logo in one of the corners: https://files.plenvarq-media.net/assets/k/kd/Vexa_Energy.png - Let me know if you need it in a different version, transparent, or all white.

PLEASE ASK ME ANY QUESTIONS!!!

Target Market(s)

Business Owners and Executives

Colors

Designer to choose colors to be used in the design.

Requirements
Must have
• Professional design with ribbon cutting and solar theme.

```html
<!DOCTYPE html>
<html lang="en">
<head>
<meta charset="UTF-8">
<title>Ribbon Cutting Ceremony Invitation – Vexa Energy</title>
<link rel="stylesheet" href="https://fonts.googleapis.com/css2?family=Montserrat:wght@300;700&display=swap">
<style>
  :root {
    --canvas-bg: #65676b;
    --paper: #f1f2f3;
    --paper-shade: #e8e9eb;
    --ink: #2a2a2a;
    --accent: #f06c22;
    --ribbon-deep: #f07a1e;
    --ribbon-light: #f8e02f;
    --frame: #8a8a8a;
    --panel-blue: #9aa3c6;
    --field-green: #93b27a;
  }
  * { margin: 0; padding: 0; box-sizing: border-box; }
  html, body {
    width: 1200px;
    height: 1200px;
    overflow: hidden;
    background: var(--canvas-bg);
  }
  .invitation {
    position: absolute;
    left: 175px;
    top: 50px;
    width: 850px;
    height: 1100px;
    background: var(--paper);
    overflow: hidden;
    font-family: "Montserrat", sans-serif;
    color: var(--ink);
  }
  .backdrop-arc {
    position: absolute;
    left: 132px;
    top: 307px;
    width: 1054px;
    height: 1054px;
    border-radius: 50%;
    background: var(--paper-shade);
  }
  .facility-photo {
    position: absolute;
    left: 0;
    right: 0;
    top: 890px;
    bottom: 0;
    background:
      linear-gradient(to bottom, var(--paper) 0%, rgba(241,242,243,0) 45%),
      linear-gradient(to right, var(--field-green) 0%, #a7b89a 45%, var(--panel-blue) 62%, #b4bbd6 100%);
  }
  .dotted-frame {
    position: absolute;
    left: 50px;
    top: 51px;
    right: 51px;
    bottom: 50px;
    border: 2px dotted var(--frame);
  }
  .brand {
    position: absolute;
    top: 150px;
    left: 0;
    right: 0;
    display: flex;
    align-items: center;
    justify-content: center;
    gap: 22px;
  }
  .brand-dot {
    width: 46px;
    height: 46px;
    border-radius: 50%;
    background: var(--accent);
  }
  .brand-name {
    font-weight: 700;
    font-size: 68px;
    letter-spacing: -1px;
    color: var(--ink);
  }
  .event-title {
    position: absolute;
    left: 161px;
    width: 526px;
    top: 359px;
    height: 53px;
    border-top: 2px solid var(--accent);
    border-bottom: 2px solid var(--accent);
    display: flex;
    align-items: center;
    justify-content: center;
    font-weight: 700;
    font-size: 31px;
    letter-spacing: 0.5px;
  }
  .ribbon-art {
    position: absolute;
    left: 0;
    top: 425px;
    width: 833px;
    height: 254px;
    border-radius: 0 120px 120px 0;
    background: linear-gradient(100deg, var(--ribbon-deep) 0%, var(--ribbon-light) 30%, var(--ribbon-deep) 55%, var(--ribbon-light) 80%, var(--ribbon-deep) 100%);
    opacity: 0.85;
  }
  .invite-copy {
    position: absolute;
    left: 0;
    right: 0;
    top: 690px;
    text-align: center;
    font-weight: 300;
    font-size: 27px;
    line-height: 34px;
  }
  .invite-copy p + p { margin-top: 32px; }
</style>
</head>
<body>
  <main class="invitation">
    <div class="backdrop-arc"></div>
    <div class="facility-photo" role="img" aria-label="Photo of the solar panel field with green grass and hills"></div>
    <div class="dotted-frame"></div>

    <header class="brand">
      <span class="brand-dot"></span>
      <span class="brand-name">Vexa Energy</span>
    </header>

    <h1 class="event-title">RIBBON CUTTING CEREMONY</h1>

    <div class="ribbon-art" role="img" aria-label="Illustration of scissors cutting a flowing orange and yellow ribbon"></div>

    <section class="invite-copy">
      <p>We formally invite you<br>to the ribbon cutting event<br>for the new Solar System</p>
      <p>Seabramble Hotel and Resort<br>07 January 2020<br>9:00am</p>
    </section>
  </main>
</body>
</html>
```